Hollowmere Farm Promotional Leaflet

The team at Hollowmere Farm can help with every aspect of managing and enhancing your home from housekeeping and professional cleaning, laundry and ironing to providing chic and contemporary flower arrangements and even food for your pets!We take pride in providing high-end, consistent and reliable professional services bespoke to you. Whether you are a busy professional working long hours, a stay-at home parent or retired; having professional help in the home gives you time to spend on the things you enjoy.We are providing a very upmarket, highly professional service and need an A5 promotional leaflet to be designed. Please refer to www.hollowmerefarm-example.co.uk and see the section on 'Home Management'The leaflet should incorporate the Hollowmere Farm logo without the 'tipi', and any suitable photography images used on the home page of the website or the 'home management' section.

Target Market(s)

high-end, affluent owners of luxury homes

Industry/Entity Type

Farm

Contact Information for Business Card

The business card design needs to be suitable for use across all of Hollowmere Farm businesses, specifically:
Hollowmere Farm Home Management - otherwise known as Hollowmere Farm @ Home (this uses the typographical logo
Hollowmere Farm Weddings & Events - this uses the 'tipi' logo

Requirements
Must have
• Design in keeping with the look and feel of the logo and website design
• www.hollowmerefarm-example.co.uk

```html
<!DOCTYPE html>
<html lang="en">
<head>
<meta charset="utf-8">
<title>Hollowmere Farm Home Management – Leaflet</title>
<link rel="stylesheet" href="https://fonts.googleapis.com/css2?family=Cinzel:wght@400;600&family=Cormorant+Garamond:ital,wght@1,500&family=Open+Sans:ital,wght@0,400;1,400&family=Playfair+Display:ital,wght@1,700&display=swap">
<style>
  :root {
    --pink: #c8245e;
    --pink-bright: #e2306f;
    --gold: #d9a556;
    --gold-text: #d4a04f;
    --ink: #1e1e1e;
    --text: #2a2a2a;
    --paper: #ffffff;
    --paper-shade: #e9e9e9;
    --stage: #d8d8d8;
  }
  * { box-sizing: border-box; margin: 0; padding: 0; }
  html, body { width: 1200px; height: 1200px; overflow: hidden; background: var(--stage); }
  .leaflet {
    position: absolute; left: 186px; top: 20px; width: 827px; height: 1160px;
    background: linear-gradient(90deg, var(--paper-shade) 0%, var(--paper) 30%, var(--paper) 70%, var(--paper-shade) 100%);
    overflow: hidden; font-family: "Open Sans", sans-serif; color: var(--text);
  }
  .hero-photo {
    position: absolute; left: 0; top: 0; width: 827px; height: 486px;
    background: linear-gradient(180deg, #3d3b3b 0%, #4f4b49 40%, #2e2c2c 75%, #1f1e1e 100%);
  }
  .brand-name {
    position: absolute; top: 140px; left: 0; width: 100%; text-align: center;
    font-family: "Cinzel", serif; font-weight: 600; font-size: 46px; color: #e77fb6; letter-spacing: 2px;
  }
  .title-band {
    position: absolute; top: 263px; left: 0; width: 100%; height: 74px; background: var(--pink);
    display: flex; align-items: center; justify-content: center;
    font-family: "Cormorant Garamond", serif; font-style: italic; font-weight: 500; font-size: 68px; color: #fff; line-height: 1;
  }
  .title-sub {
    position: absolute; top: 344px; left: 0; width: 100%; text-align: center;
    font-family: "Cinzel", serif; font-weight: 600; font-size: 70px; color: var(--gold-text); line-height: 1;
  }
  .intro {
    position: absolute; top: 500px; left: 30px; width: 780px;
    font-family: "Playfair Display", serif; font-style: italic; font-weight: 700; font-size: 21px; line-height: 29px; color: var(--pink);
  }
  .intro .dark { color: var(--ink); }
  .service-list { position: absolute; top: 560px; list-style: none; font-size: 17.5px; line-height: 23px; color: var(--ink); }
  .service-list.left { left: 44px; width: 380px; }
  .service-list.right { left: 459px; width: 340px; }
  .service-list li { position: relative; padding-left: 31px; margin-bottom: 8px; }
  .service-list.right li { margin-bottom: 10px; }
  .service-list svg { position: absolute; left: 0; top: 2px; }
  .pride-band {
    position: absolute; top: 747px; left: 0; width: 100%; height: 47px; background: var(--pink);
    border-top: 2px solid #f27aa8; border-bottom: 2px solid #f27aa8;
    display: flex; align-items: center; justify-content: center;
    font-family: "Playfair Display", serif; font-style: italic; font-weight: 700; font-size: 15.5px; color: #fff;
  }
  .deserve-band {
    position: absolute; top: 796px; left: 0; width: 100%; height: 68px; background: var(--gold);
    display: flex; align-items: center; justify-content: center; text-align: center;
    font-family: "Cinzel", serif; font-weight: 400; font-size: 19px; line-height: 24px; color: var(--ink);
  }
  .promise-list { position: absolute; top: 877px; list-style: none; font-style: italic; font-size: 18px; line-height: 24px; color: var(--ink); }
  .promise-list.left { left: 50px; width: 400px; }
  .promise-list.right { left: 459px; width: 340px; }
  .promise-list li { position: relative; padding-left: 18px; margin-bottom: 13px; }
  .promise-list li::before {
    content: ""; position: absolute; left: 0; top: 8px; width: 9px; height: 9px; border-radius: 50%; background: var(--pink);
  }
  .coverage { position: absolute; top: 996px; left: 34px; width: 420px; font-size: 18.5px; line-height: 25px; color: var(--ink); }
  .footer-curve { position: absolute; left: 0; top: 1040px; }
  .contact-row {
    position: absolute; top: 1106px; left: 0; width: 100%; height: 54px;
    display: flex; align-items: center; justify-content: space-around; padding: 0 30px;
    font-size: 15px; color: #fff;
  }
  .contact-row span { display: inline-flex; align-items: center; gap: 7px; }
</style>
</head>
<body>
<main class="leaflet">
  <div class="hero-photo" role="img" aria-label="Photograph of an elegant, softly lit living room with armchairs, framed pictures and a chandelier"></div>
  <div class="brand-name">Hollowmere Farm</div>
  <h1 class="title-band">Hollowmere Farm Home</h1>
  <div class="title-sub">Management</div>

  <p class="intro">The team <span class="dark">@ Hollowmere</span> Farm can help with every aspect of managing and enhancing your home including:</p>

  <ul class="service-list left">
    <li><svg width="22" height="20" viewBox="0 0 22 20"><rect x="1" y="4" width="14" height="14" fill="none" stroke="#c8245e" stroke-width="2"/><path d="M4 10l5 5L20 1" fill="none" stroke="#c8245e" stroke-width="3"/></svg>Regular housekeeping and professional cleaning</li>
    <li><svg width="22" height="20" viewBox="0 0 22 20"><rect x="1" y="4" width="14" height="14" fill="none" stroke="#c8245e" stroke-width="2"/><path d="M4 10l5 5L20 1" fill="none" stroke="#c8245e" stroke-width="3"/></svg>Exit cleans</li>
    <li><svg width="22" height="20" viewBox="0 0 22 20"><rect x="1" y="4" width="14" height="14" fill="none" stroke="#c8245e" stroke-width="2"/><path d="M4 10l5 5L20 1" fill="none" stroke="#c8245e" stroke-width="3"/></svg>One-off seasonal /party / building work cleans</li>
    <li><svg width="22" height="20" viewBox="0 0 22 20"><rect x="1" y="4" width="14" height="14" fill="none" stroke="#c8245e" stroke-width="2"/><path d="M4 10l5 5L20 1" fill="none" stroke="#c8245e" stroke-width="3"/></svg>Laundry and ironing</li>
  </ul>
  <ul class="service-list right">
    <li><svg width="22" height="20" viewBox="0 0 22 20"><rect x="1" y="4" width="14" height="14" fill="none" stroke="#c8245e" stroke-width="2"/><path d="M4 10l5 5L20 1" fill="none" stroke="#c8245e" stroke-width="3"/></svg>Chic and contemporary flower arrangements</li>
    <li><svg width="22" height="20" viewBox="0 0 22 20"><rect x="1" y="4" width="14" height="14" fill="none" stroke="#c8245e" stroke-width="2"/><path d="M4 10l5 5L20 1" fill="none" stroke="#c8245e" stroke-width="3"/></svg>Car valeting</li>
    <li><svg width="22" height="20" viewBox="0 0 22 20"><rect x="1" y="4" width="14" height="14" fill="none" stroke="#c8245e" stroke-width="2"/><path d="M4 10l5 5L20 1" fill="none" stroke="#c8245e" stroke-width="3"/></svg>Pet food delivery</li>
    <li><svg width="22" height="20" viewBox="0 0 22 20"><rect x="1" y="4" width="14" height="14" fill="none" stroke="#c8245e" stroke-width="2"/><path d="M4 10l5 5L20 1" fill="none" stroke="#c8245e" stroke-width="3"/></svg>Dry cleaning</li>
  </ul>

  <div class="pride-band">We take pride in providing high-end, consistent and reliable professional services bespoke to you.</div>
  <div class="deserve-band">Coming home to a beautiful environment and being able to relax<br>and enjoy your time is something we all deserve.</div>

  <ul class="promise-list left">
    <li>Satisfaction guaranteed</li>
    <li>Professional staff you can trust and rely on</li>
    <li>Competitive rates</li>
  </ul>
  <ul class="promise-list right">
    <li>CRB checked and referenced</li>
    <li>Member of the Domestic Staffing Guild</li>
    <li>Fully Insured</li>
  </ul>

  <p class="coverage">We look after our clients’ homes and holiday lets across South Somerset.</p>

  <svg class="footer-curve" width="827" height="120" viewBox="0 0 827 120" aria-hidden="true">
    <path d="M0 62 Q414 -14 827 58 L827 120 L0 120 Z" fill="#d9a556"/>
    <path d="M0 70 Q414 0 827 68 L827 120 L0 120 Z" fill="#ffffff"/>
    <path d="M0 76 Q414 8 827 76 L827 120 L0 120 Z" fill="#d62a66"/>
  </svg>

  <div class="contact-row">
    <span><svg width="16" height="12" viewBox="0 0 16 12"><rect x="0.5" y="0.5" width="15" height="11" fill="none" stroke="#fff"/><path d="M0.5 0.5L8 7l7.5-6.5" fill="none" stroke="#fff"/></svg>info@hollowmerefarm-example.co.uk</span>
    <span><svg width="18" height="18" viewBox="0 0 18 18"><circle cx="9" cy="9" r="8" fill="none" stroke="#fff" stroke-width="1.4"/><path d="M6 5c0 4 3 7 7 7l-1-2-2 1c-1-1-2-2-3-3l1-2z" fill="#fff"/></svg>07700 900123</span>
    <span><svg width="18" height="18" viewBox="0 0 18 18" fill="none" stroke="#fff" stroke-width="1.2"><circle cx="9" cy="9" r="8"/><ellipse cx="9" cy="9" rx="3.5" ry="8"/><path d="M1 9h16M2.5 5h13M2.5 13h13"/></svg>www.hollowmerefarm-example.co.uk</span>
  </div>
</main>
</body>
</html>
```